Business Card Design Project for Architecture and Interior Design company

We need a business card design and logo for an architecture and design firm located in Santiago de Chile. It´s a small company, and the name is "Ostrevo" ("Ostr" from my surname Ostrini, and "arq" for arquitectura or architecture. But it would also be nice that the logo comunicates de Word game "Bella" as beautiful in italian, and "arq" as architecture".
The idea is to give a delicate, elegant and sofisticated, yet fresh image. Would prefer grey black and white colors, but wouldn´t mind to use another additional color.
I allready have a web page www.ostrevo-studio.example, but would like to improve the logo design.
Please contact if any further information is requiered.
Reason: Need a more arquitectural and desing spirit in the cards. Few of them give that idea.

```html
<!DOCTYPE html>
<html lang="es">
<head>
<meta charset="utf-8">
<title>Ostrevo – Tarjeta de presentación</title>
<link href="https://fonts.googleapis.com/css2?family=Delius&display=swap" rel="stylesheet">
<style>
  :root {
    --paper: #ffffff;
    --ink: #2e2e2e;
    --plum: #4a1f40;
    --arch-light: #f4f3f3;
    --arch-mid: #e6e4e5;
  }
  html, body {
    margin: 0;
    padding: 0;
    overflow: hidden;
    background: var(--paper);
  }
  .card {
    position: relative;
    width: 1200px;
    height: 842px;
    background: var(--paper);
    font-family: "Delius", cursive;
    overflow: hidden;
  }
  .arcade-illustration {
    position: absolute;
    left: 168px;
    top: 36px;
    width: 864px;
    height: 510px;
    border-radius: 380px 380px 12px 12px;
    background: linear-gradient(180deg, var(--arch-light) 0%, var(--arch-mid) 100%);
  }
  .brand-name {
    position: absolute;
    left: 0;
    width: 1200px;
    top: 392px;
    text-align: center;
    font-size: 60px;
    line-height: 1;
    color: var(--ink);
    margin: 0;
    font-weight: 400;
  }
  .contact-list {
    position: absolute;
    left: 186px;
    top: 588px;
    margin: 0;
    padding: 0;
    list-style: none;
  }
  .contact-item {
    display: flex;
    align-items: center;
    height: 62px;
    font-size: 26px;
    color: var(--plum);
  }
  .contact-icon {
    width: 56px;
    height: 44px;
    margin-right: 26px;
    flex: none;
  }
  .contact-icon * {
    fill: none;
    stroke: var(--ink);
    stroke-width: 2.4;
    stroke-linejoin: round;
    stroke-linecap: round;
  }
  .holder {
    position: absolute;
    right: 195px;
    top: 582px;
    text-align: right;
    color: var(--ink);
  }
  .holder-name {
    margin: 0;
    font-size: 46px;
    line-height: 72px;
    font-weight: 400;
  }
  .holder-role {
    margin: 8px 0 0;
    font-size: 26px;
    color: var(--plum);
  }
</style>
</head>
<body>
  <main class="card">
    <div class="arcade-illustration" role="img" aria-label="Hand-drawn arcade of three stone arches resting on Ionic columns"></div>
    <h1 class="brand-name">Ostrevo</h1>

    <ul class="contact-list">
      <li class="contact-item">
        <svg class="contact-icon" viewBox="0 0 56 44" aria-hidden="true">
          <path d="M28 6c-11 0-19 7-19 16 0 8 6 14 15 15l-2 6 8-6c10-1 17-7 17-15 0-9-8-16-19-16z"/>
        </svg>
        <span>+56 9 55501234</span>
      </li>
      <li class="contact-item">
        <svg class="contact-icon" viewBox="0 0 56 44" aria-hidden="true">
          <rect x="4" y="9" width="48" height="28"/>
          <path d="M4 9l24 17 24-17"/>
        </svg>
        <span>aostrini@ostrevo-studio.example</span>
      </li>
      <li class="contact-item">
        <svg class="contact-icon" viewBox="0 0 56 44" aria-hidden="true">
          <circle cx="28" cy="22" r="18"/>
          <path d="M12 16c6 2 8 6 6 10M34 6c-4 4-2 8 4 9M30 38c0-6 4-8 8-6"/>
        </svg>
        <span>www.ostrevo-studio.example</span>
      </li>
    </ul>

    <section class="holder">
      <p class="holder-name">Anjali Ostrini<br>Ramdev</p>
      <p class="holder-role">Arquitecto</p>
    </section>
  </main>
</body>
</html>
```